Thai Restaurant Billboard Design

Design a billboard promoting food delivery during this Coronavirus time. We want to grab attention by embracing the Coronavirus and offering food delivery. People are sitting at home and this is the right time to promote food delivery.

I have the logo and spec sheet attached.

Target Market(s)

Anyone.

Requirements
Must have
• Top Heading should be big and bold:

Coronavirus Got You Quarantined?

Then put under

We Deliver
Healthy Thai Food!
Put the logo that is attached
415-283-6071
Nice to have
• Eyecatching. Creative.
Should not have
• Don't have any not haves. Make it look good.

```html
<!DOCTYPE html>
<html lang="en">
<head>
<meta charset="utf-8">
<title>Thai Delivery Billboard</title>
<link href="https://fonts.googleapis.com/css2?family=Oswald:wght@600;700&display=swap" rel="stylesheet">
<style>
  :root {
    --page: #eef1f4;
    --red: #c8102e;
    --red-deep: #a50d26;
    --yellow: #fcd116;
    --amber: #f9a81b;
    --bowl-dark: #2a1416;
    --bowl-warm: #c2461d;
  }
  html, body {
    margin: 0;
    width: 1200px;
    height: 840px;
    overflow: hidden;
    background: var(--page);
  }
  .billboard {
    position: absolute;
    left: 30px;
    top: 236px;
    width: 1140px;
    height: 368px;
    overflow: hidden;
    background: linear-gradient(100deg, var(--amber) 0%, var(--yellow) 45%, var(--amber) 100%);
    font-family: "Oswald", "Arial Narrow", sans-serif;
  }
  .red-field {
    position: absolute;
    inset: 0;
  }
  .headline {
    position: absolute;
    left: 62px;
    top: 30px;
    margin: 0;
    color: var(--yellow);
    font-weight: 700;
    font-style: oblique 10deg;
    font-size: 54px;
    line-height: 1.1;
    text-transform: uppercase;
    letter-spacing: 0.5px;
    white-space: nowrap;
    z-index: 2;
  }
  .offer {
    position: absolute;
    left: 58px;
    top: 214px;
    margin: 0;
    color: var(--red);
    font-weight: 700;
    font-style: oblique 10deg;
    text-transform: uppercase;
    line-height: 1;
    white-space: nowrap;
  }
  .offer-main { display: block; font-size: 62px; }
  .offer-sub { display: block; font-size: 34px; margin-top: 4px; }
  .dish-photo {
    position: absolute;
    left: 445px;
    top: 160px;
    width: 300px;
    height: 190px;
    border-radius: 18px 18px 56px 56px;
    background: radial-gradient(ellipse at 50% 22%, var(--bowl-warm) 0%, #7a2a1a 38%, var(--bowl-dark) 70%);
  }
  .brand {
    position: absolute;
    left: 790px;
    top: 110px;
    width: 300px;
    display: flex;
    align-items: center;
    justify-content: center;
    gap: 12px;
    color: var(--red);
    font-weight: 700;
    font-size: 30px;
    text-transform: uppercase;
    white-space: nowrap;
  }
  .brand-mark {
    width: 20px;
    height: 20px;
    background: var(--red);
    flex: none;
  }
  .phone {
    position: absolute;
    left: 770px;
    top: 272px;
    margin: 0;
    color: var(--red);
    font-weight: 700;
    font-style: oblique 10deg;
    font-size: 40px;
    letter-spacing: 0.5px;
    white-space: nowrap;
  }
</style>
</head>
<body>
  <section class="billboard">
    <svg class="red-field" width="1140" height="368" viewBox="0 0 1140 368" aria-hidden="true">
      <defs>
        <linearGradient id="redBand" x1="0" y1="0" x2="1" y2="0">
          <stop offset="0" stop-color="#a50d26"/>
          <stop offset="1" stop-color="#d81e34"/>
        </linearGradient>
      </defs>
      <path d="M0 0 H870 C760 70 560 130 300 175 C180 195 80 210 0 228 Z" fill="url(#redBand)"/>
    </svg>

    <h1 class="headline">Coronavirus got you<br>quarantined?</h1>

    <p class="offer">
      <span class="offer-main">We deliver</span>
      <span class="offer-sub">Healthy Thai food!</span>
    </p>

    <div class="dish-photo" role="img" aria-label="Steaming bowl of stir-fried Thai noodles with a fried egg and chopsticks"></div>

    <div class="brand">
      <span class="brand-mark"></span>
      <span class="brand-name">Siam Lotus Kitchen</span>
    </div>

    <p class="phone">CALL: 415-283-6071</p>
  </section>
</body>
</html>
```